Small Batch Ice Cream Shop Needs a PINT label

We need a PINT label for a homemade ice cream shop based in Tianjin, China called " PEPPER & FIG". We purchased the whole white paper pint container and we are going to stick the label at the front and on the top of the PINT. Below are the pictures of our container,logo, shop front door and the lid that we made our self to give a feel that what we want. We want to deliver a massage that we make fresh, healthy, and serious frozen dessert. There should be a blank space in the middle of the label that we can hand write our flavors. We want to use different color for different flavor. The slogan “Small Batch Ice Cream Made With Love" needed to be on the label, better underneath the logo. We use Trajan Pro Bold, word space 1bl for our label. Please attention: The whole front label should be seeable when we close the lid, so please be careful the margin. The whole theme of the label should be fresh and delicacy.
Some pics attached just give you some ideas what we want, but I am open to any great ideas. Thanks!!

Project Deadline Extended Reason: brief has been changed; therefore, I extend the deadline. Added Tuesday, August 11, 2015

Reason: I don't have enough designs choose from. I would like to attract more designers . Thanks

Target Market(s)

18-35 years students and working class

Industry/Entity Type

Shop

Requirements
Must have
• logo
• slogan "Small Batch Ice Cream Made With Love"
• slogan "Fresh l Healthy l Serious " at the bottom
• "1 Pint (473ml)" at the bottom
Nice to have
• nice to have some decorative pattern
• different color theme for different flavors:
• flavors we have so far: Durian ;Salted Caramel; Honey Lavender; London Fog; Whisk Hazelnut; Chocolate Brownie; Balsamic Strawberry; Caramelized Banana

```html
<!DOCTYPE html>
<html lang="en">
<head>
<meta charset="UTF-8">
<title>Pepper &amp; Fig – Pint Labels</title>
<link rel="stylesheet" href="https://fonts.googleapis.com/css2?family=Cinzel:wght@400;700&family=Open+Sans:wght@400&family=Oswald:wght@400;500&display=swap">
<style>
  :root {
    --page: #ffffff;
    --coral: #e46e6c;
    --coral-deep: #dd6264;
    --blush: #f3b6b8;
    --rim: #b8262c;
    --rim-soft: #f2c4c4;
    --ink-light: #ffffff;
    --ink-dark: #2a1a1a;
  }
  * { box-sizing: border-box; margin: 0; padding: 0; }
  html, body { width: 900px; height: 1200px; overflow: hidden; background: var(--page); }
  .sheet { position: relative; width: 900px; height: 1200px; }

  /* Lid label */
  .lid-label { position: absolute; left: 200px; top: 30px; width: 500px; height: 500px; }
  .lid-label svg { position: absolute; inset: 0; }
  .lid-text { position: absolute; inset: 0; text-align: center; color: var(--ink-light); }
  .lid-title {
    position: absolute; top: 212px; width: 100%;
    font-family: "Cinzel", serif; font-weight: 400; font-size: 42px; letter-spacing: 1px; word-spacing: 6px;
  }
  .lid-slogan {
    position: absolute; top: 280px; width: 100%;
    font-family: "Open Sans", sans-serif; font-size: 17px;
  }
  .lid-volume {
    position: absolute; top: 398px; width: 100%;
    font-family: "Oswald", sans-serif; font-size: 30px;
  }

  /* Front label */
  .front-label {
    position: absolute; left: 186px; top: 570px; width: 534px; height: 612px;
    background: var(--coral); color: var(--ink-light);
  }
  .front-pattern { position: absolute; inset: 0; background: linear-gradient(180deg, var(--coral) 0%, var(--coral-deep) 100%); }
  .front-title {
    position: absolute; top: 46px; width: 100%; text-align: center;
    font-family: "Cinzel", serif; font-size: 54px; letter-spacing: 1px; word-spacing: 8px;
  }
  .front-slogan {
    position: absolute; top: 135px; width: 100%; text-align: center;
    font-family: "Open Sans", sans-serif; font-size: 20px;
  }
  .flavor-window { position: absolute; left: 82px; top: 222px; width: 370px; height: 220px; }
  .front-footer {
    position: absolute; left: 24px; right: 28px; bottom: 24px;
    display: flex; justify-content: space-between; align-items: baseline;
    font-family: "Oswald", sans-serif; color: var(--ink-dark);
  }
  .front-tagline { font-size: 20px; font-weight: 500; }
  .front-volume { font-size: 34px; color: var(--ink-light); }
</style>
</head>
<body>
<main class="sheet">

  <section class="lid-label">
    <svg viewBox="0 0 500 500" width="500" height="500">
      <circle cx="250" cy="250" r="248" fill="var(--blush)" role="img" aria-label="Light pink decorative floral pattern border"/>
      <circle cx="250" cy="250" r="200" fill="var(--coral)" role="img" aria-label="Coral decorative floral pattern background"/>
    </svg>
    <div class="lid-text">
      <h2 class="lid-title">PEPPER &amp; FIG</h2>
      <p class="lid-slogan">Small Batch Ice Cream Made With Love</p>
      <p class="lid-volume">473ml</p>
    </div>
  </section>

  <section class="front-label">
    <div class="front-pattern" role="img" aria-label="Coral decorative floral pattern background"></div>
    <h1 class="front-title">PEPPER &amp; FIG</h1>
    <p class="front-slogan">Small Batch Ice Cream Made With Love</p>
    <svg class="flavor-window" viewBox="0 0 370 220" width="370" height="220" aria-label="Blank space for handwritten flavor">
      <ellipse cx="185" cy="110" rx="183" ry="108" fill="var(--rim-soft)"/>
      <ellipse cx="185" cy="110" rx="176" ry="101" fill="var(--rim)"/>
      <ellipse cx="185" cy="110" rx="164" ry="90" fill="#ffffff"/>
    </svg>
    <div class="front-footer">
      <span class="front-tagline">Fresh l Healthy l Serious</span>
      <span class="front-volume">473ml</span>
    </div>
  </section>

</main>
</body>
</html>
```